Independent manufacturing consultant needs a professional Logo & biz card Update

I want a new logo using the existing one as inspiration. The company legal name is Brindlecourt Process Advisory & Engineering Group, Inc. Often the name is shortened to Brindlecourt PAE and that matches with web address of www.brindlecourt-pae.example. #1 create a new logo and #2 update biz card. I will need vector file to get cards printed (bilingual English & Japanese). The reverse side will be an exact copy of the original design but in Japanese. I have another resource for the translation so that is not in this scope.
Next month, a follow-up project will be to update the website using new logo and get a professional, cohesive look to all the pages.
Check out web site to get an idea of what we do. The desire is to project professional, articulate, clean, dependable, detailed oriented team of experts.

Target Market(s)

Food and Beverage manufactures. Major players, regiona, and start ups.

Industry/Entity Type

It Company

Contact Information for Business Card

exisiting card and logo provided as foundation but ready to improve upon both!

Logo Text

Brindlecourt PAE or other....

Font styles to use
Sans Serif

Colors
9bcb3c
0356a4

Requirements
Must have
• Logo and biz card.
• Logo will be used for other materials and website.
Nice to have
• open to suggestions.
• Like the Green & Blue colors but also dig grey scale as the website incorporates.
• Open to suggestions.
Should not have
• not to animated. I work with more conservative clients.

```html
<!DOCTYPE html>
<html lang="en">
<head>
<meta charset="utf-8">
<title>Brindlecourt PAE – Business Card</title>
<link rel="stylesheet" href="https://fonts.googleapis.com/css2?family=Questrial&family=Open+Sans:wght@400;600&display=swap">
<style>
  :root {
    --brand-blue: #0356a4;
    --brand-green: #9bcb3c;
    --ink-dark: #2f3133;
    --band-grey: #3a3c3f;
    --card-white: #ffffff;
    --card-grey: #e3e4e6;
    --backdrop: #d9d6d0;
  }
  * { box-sizing: border-box; margin: 0; padding: 0; }
  html, body {
    width: 1200px;
    height: 1020px;
    overflow: hidden;
    background: var(--backdrop);
  }
  .canvas {
    position: relative;
    width: 1200px;
    height: 1020px;
  }
  .card {
    position: absolute;
    left: 75px;
    top: 210px;
    width: 1050px;
    height: 600px;
    background: linear-gradient(115deg, var(--card-white) 0%, var(--card-white) 45%, var(--card-grey) 100%);
    box-shadow: 0 10px 30px rgba(0,0,0,0.18);
    overflow: hidden;
  }
  .brand {
    position: absolute;
    left: 62px;
    top: 190px;
  }
  .brand-name {
    display: flex;
    align-items: center;
    gap: 14px;
    font-family: "Questrial", sans-serif;
    font-size: 56px;
    letter-spacing: 2px;
    color: var(--brand-blue);
    line-height: 1;
  }
  .brand-dot {
    width: 26px;
    height: 26px;
    border-radius: 50%;
    background: var(--brand-green);
  }
  .brand-tagline {
    margin-top: 14px;
    margin-left: 40px;
    font-family: "Open Sans", sans-serif;
    font-weight: 600;
    font-size: 16px;
    color: var(--brand-green);
  }
  .person {
    position: absolute;
    left: 640px;
    top: 105px;
    padding-left: 26px;
    border-left: 9px solid var(--brand-green);
  }
  .person-name {
    font-family: "Questrial", sans-serif;
    font-size: 50px;
    color: var(--ink-dark);
    line-height: 1;
  }
  .person-title {
    margin-top: 6px;
    font-family: "Questrial", sans-serif;
    font-size: 24px;
    letter-spacing: 1px;
    color: var(--brand-blue);
  }
  .contacts {
    position: absolute;
    left: 640px;
    top: 300px;
    list-style: none;
    font-family: "Open Sans", sans-serif;
    font-size: 23px;
    color: var(--ink-dark);
  }
  .contacts li {
    display: flex;
    align-items: center;
    gap: 20px;
    height: 42px;
  }
  .contacts svg {
    width: 22px;
    height: 22px;
    flex: none;
  }
  .bands {
    position: absolute;
    left: 0;
    bottom: 0;
    width: 1050px;
    height: 60px;
  }
</style>
</head>
<body>
<main class="canvas">
  <section class="card" aria-label="Business card front">
    <div class="brand">
      <div class="brand-name"><span class="brand-dot"></span>Brindlecourt PAE</div>
      <p class="brand-tagline">Brindlecourt Process Advisory &amp; Engineering Group, Inc.</p>
    </div>

    <div class="person">
      <h1 class="person-name">Dana Whitlock</h1>
      <p class="person-title">PRINCIPAL</p>
    </div>

    <ul class="contacts">
      <li>
        <svg viewBox="0 0 24 24" aria-hidden="true"><path fill="#9bcb3c" d="M3 9c0-3 4-5 9-5s9 2 9 5v2h-5V9H8v2H3zM6 12h12l2 8H4z"/><circle cx="12" cy="16" r="2.2" fill="#fff"/></svg>
        <span>555.014.2863</span>
      </li>
      <li>
        <svg viewBox="0 0 24 24" aria-hidden="true"><rect x="2" y="5" width="20" height="14" fill="#9bcb3c"/><path d="M2 5l10 8 10-8" fill="none" stroke="#fff" stroke-width="1.6"/></svg>
        <span>dana@brindlecourt-pae.example</span>
      </li>
      <li>
        <svg viewBox="0 0 24 24" aria-hidden="true"><g fill="none" stroke="#9bcb3c" stroke-width="1.6"><circle cx="12" cy="12" r="9"/><ellipse cx="12" cy="12" rx="4" ry="9"/><path d="M3 12h18M5 7h14M5 17h14"/></g></svg>
        <span>www.brindlecourt-pae.example</span>
      </li>
    </ul>

    <svg class="bands" viewBox="0 0 1050 60" preserveAspectRatio="none" aria-hidden="true">
      <polygon points="0,0 600,0 622,60 0,60" fill="var(--brand-blue)"/>
      <polygon points="618,0 1050,0 1050,60 640,60" fill="var(--band-grey)"/>
    </svg>
  </section>
</main>
</body>
</html>
```